Commercial Industrial Electrical Contractor Brochure

Need a brochure for our Commercial Electrical Contracting company that has been serving the St. Louis and surrounding area for 29 years focused on commercial construction, high end residential properties and service work. Our staff consists of full time electricians that have on average worked for our company for over 10 years. PWB is a family owned and operated electrical contractor insuring our customers receive the highest level of service and expertise in the electrical field. Our project managers have received the best electrical training in the St. Louis area having attended both the QTA apprenticeship program, the UVKR Branch seven training school, hold UVKR Journeyman A cards, and certificates of training in specialized control fields.

We strive to develop strong long term working relationships with our customers and the contractors we work with. We also have an excellent reputation with the local inspectors and a 100% on time completion record on all our projects.

Safety is very important with PWB and we have an excellent industry safety record currently at .94 experience rating which is below the national average of 1.0.

Some of recent work includes Hollin's Grocery Store in Rock Hill, MO; Thrift-N-Go Grocery Stores in Lemay, Pacific, and St. Clair, MO; Marden Foods in St. Louis, MO; KRVDS Module Rail Training Center in O'Fallon, MO; Baxters Wren Restaurant and Winery, Town and Country, MO and several educational facilities and numerous Penny Corner, Cent Central, Vortel Loaf, Burgundos, and Pellington's Bakeries and the first Gus Brantley's in the St. Louis area to name a few.

Would like to have brochure in navy, teal with some yellow and black as these are our letterhead colors. Also would like the St. Louis skyline included in the front of the brochure as our website includes. You can learn more about our company at pwbvoltworks.example. Please also include our logo attached

Target Market(s)

General Contractors, Developers, Architects

Industry/Entity Type

Electrical

Font styles to use
Sans Serif

Colors
33b8a4
0255a3
fbee3d

Requirements
Must have
• Good Photo of St. Louis Skyline and Commercial Construction Photos
Nice to have
• Industry specific details of work we do including grocery stores, retail stores, restaurants, medical facilities. Details about our excellent safety record.
Should not have
• Residential Construction Photo's or Marketing

```html
<!DOCTYPE html>
<html lang="en">
<head>
<meta charset="utf-8">
<title>PWB Contracting &amp; Services – Brochure</title>
<link rel="stylesheet" href="https://fonts.googleapis.com/css2?family=Open+Sans:wght@400;600;700&family=Oswald:wght@400;500&display=swap">
<style>
  :root {
    --bg: #d9dadc;
    --navy: #1d1f2e;
    --mint: #5ef0a3;
    --yellow: #f6ef2a;
    --white: #ffffff;
    --text-light: #d6d8e0;
    --brand-teal: #33b8a4;
    --brand-blue: #0255a3;
    --sky-top: #3f4f9a;
    --sky-mid: #7c86b8;
    --city-glow: #c9843a;
    --water: #1a1410;
  }
  * { box-sizing: border-box; margin: 0; padding: 0; }
  html, body { width: 1200px; height: 800px; overflow: hidden; }
  body { background: var(--bg); font-family: "Open Sans", Arial, sans-serif; position: relative; }

  .sheet { position: absolute; top: 212px; width: 575px; height: 375px; overflow: hidden; box-shadow: 0 2px 8px rgba(0,0,0,.18); }
  .sheet--outside { left: 15px; }
  .sheet--inside { left: 610px; background: var(--navy); }
  .sheet svg.shapes { position: absolute; inset: 0; width: 100%; height: 100%; }
  .abs { position: absolute; }

  /* Outside */
  .skyline-photo { position: absolute; inset: 0;
    background: linear-gradient(180deg, var(--sky-top) 0%, var(--sky-mid) 42%, #8a6f62 58%, var(--city-glow) 66%, #3a2a1c 74%, var(--water) 100%); }
  .about { left: 22px; top: 120px; width: 140px; color: var(--white); }
  .about h2 { font-family: "Oswald", Arial, sans-serif; font-weight: 400; font-size: 15px; margin-bottom: 5px; }
  .about p { font-size: 6.2px; line-height: 1.5; color: var(--text-light); }
  .brand { left: 398px; top: 150px; width: 175px; color: var(--brand-blue); }
  .brand-row { display: flex; align-items: center; gap: 5px; white-space: nowrap; }
  .brand-dot { width: 14px; height: 14px; border-radius: 50%; background: var(--brand-teal); flex: none; }
  .brand-name { font-weight: 700; font-size: 8.5px; line-height: 1.2; }
  .brand-tag { font-size: 7px; margin-top: 3px; padding-left: 19px; white-space: nowrap; }
  .footer-note { left: 0; right: 0; top: 352px; text-align: center; color: var(--text-light); font-size: 5.5px; }
  .home-icon { left: 280px; top: 337px; width: 10px; height: 10px; }

  /* Inside */
  .banner { position: absolute; background: var(--mint); color: var(--white); font-family: "Oswald", Arial, sans-serif; font-weight: 400; font-size: 9.5px; line-height: 16px; height: 16px; padding: 0 8px; white-space: nowrap; }
  .banner--center { text-align: center; }
  .banner--right { text-align: right; }
  .copy { position: absolute; color: var(--text-light); font-size: 5.8px; line-height: 1.5; }
  .copy p + p { margin-top: 6px; }
  .copy h3 { color: var(--white); font-size: 6px; font-weight: 600; margin-bottom: 2px; }
  .copy--right { text-align: right; }
  .copy--justify { text-align: justify; }
  .project-list { list-style: none; }
  .photo-diamond { position: absolute; transform: rotate(45deg); border: 1.5px solid var(--white); }
  .photo-diamond--inspect { background: linear-gradient(135deg, #c7392f, #6b7f8f 60%, #d9d2c4); }
  .photo-diamond--testing { background: linear-gradient(135deg, #e2b530, #3a6fb5 55%, #c23a2a); }
  .photo-diamond--commercial { background: linear-gradient(135deg, #8fa6c0, #dfe6ee 50%, #5a6e86); }
  .photo-diamond--residential { background: linear-gradient(135deg, #b79a7a, #e9e2d6 50%, #6b5a4a); }
  .site-url { position: absolute; color: var(--white); font-size: 8.5px; white-space: nowrap; }
</style>
</head>
<body>

<section class="sheet sheet--outside" aria-label="Brochure outside">
  <div class="skyline-photo" role="img" aria-label="St. Louis skyline at dusk with the arch and city lights reflected on the river"></div>
  <svg class="shapes" viewBox="0 0 575 375" aria-hidden="true">
    <polygon points="190,0 400,0 295,90" fill="var(--navy)"/>
    <polygon points="0,40 255,215 0,375" fill="var(--navy)"/>
    <polygon points="575,20 345,185 575,345" fill="var(--white)"/>
    <polygon points="205,375 293,300 380,375" fill="var(--navy)"/>
  </svg>
  <div class="abs about">
    <h2>About us</h2>
    <p>PWB Contracting &amp; Services, LLC is a family-owned and operated company specializing in all aspects of electrical contracting. PWB has been serving St. Louis and all surrounding counties since 1987. Starting as a humble home business with one service van, Hal and Dora Penwick founded the company as Meadowline Electric.</p>
  </div>
  <div class="abs brand">
    <div class="brand-row"><span class="brand-dot"></span><span class="brand-name">PWB Contracting &amp; Services, LLC</span></div>
    <div class="brand-tag">Electrical &amp; Service Contractor</div>
  </div>
  <svg class="abs home-icon" viewBox="0 0 10 10" aria-hidden="true"><path d="M5 1 L9.5 5 H8 V9 H6 V6.5 H4 V9 H2 V5 H0.5 Z" fill="var(--white)"/></svg>
  <p class="abs footer-note">UVKR Branch seven. Electrical Contractor located in Harlow Bend, MO</p>
</section>

<section class="sheet sheet--inside" aria-label="Brochure inside">
  <svg class="shapes" viewBox="0 0 575 375" aria-hidden="true">
    <polygon points="150,0 206,0 178,30" fill="var(--yellow)"/>
    <polygon points="295,0 355,0 325,30" fill="var(--yellow)"/>
    <polygon points="77,375 102,348 127,375" fill="var(--yellow)"/>
    <polygon points="240,375 262,350 284,375" fill="var(--yellow)"/>
    <polygon points="485,375 508,350 531,375" fill="var(--yellow)"/>
  </svg>

  <h2 class="banner" style="left:0;top:22px;width:172px;">PWB Today</h2>
  <div class="copy copy--justify" style="left:10px;top:46px;width:160px;">
    <p>Today, to more fully convey the expertise of our field, the company operates business as PWB Contracting &amp; Services, LLC doing business as PWB Electric, LLC. PWB has an excellent reputation in providing the highest quality electrical services and products with all of our contractors, customers, and the electrical inspectors in the St. Louis and surrounding counties.</p>
    <p>As a electrician in St. Louis, PWB is involved in all aspects of electrical contracting including solar panels, data, phone, fire alarm, and security wiring. We have a large portfolio of custom home wiring up to 22,000 square foot homes, tenant finish projects of all sorts, medical facilities, schools, restaurants, and explosion proof electrical systems.</p>
  </div>
  <h2 class="banner banner--center" style="left:42px;top:210px;width:138px;height:14px;line-height:14px;">A few recent PWB projects</h2>
  <ul class="copy project-list" style="left:10px;top:230px;width:165px;">
    <li>Thrift-N-Go Grocery Stores</li>
    <li>Hollin's Market – Rock Hill, MO</li>
    <li>Gus Brantley's, Maplewood, MO</li>
    <li>Baxters Wren Winery and Restaurant</li>
    <li>Ardel Ridge Vineyards, Augusta, MO</li>
    <li>Pellington's Bakeries</li>
    <li>Module Rail and KRVDS Training Facilities, O'Fallon, MO</li>
    <li>Marlow Fire House – Villa Ridge, MO</li>
    <li>Tennant Fire House – Gray Summit, MO</li>
    <li>Multiple Burgundos Café Remodels</li>
    <li>Burgundos Restaurant – St. Clair, MO</li>
  </ul>

  <h2 class="banner banner--center" style="left:182px;top:22px;width:150px;">Services</h2>
  <div class="copy" style="left:187px;top:44px;width:148px;">
    <p>You must call PWB for all of your St. Louis electrical needs! We are the St. Louis electricians to call to bring electricity or add electrical components to your factory, business, or home.</p>
    <p>Our services are:</p>
  </div>
  <div class="copy" style="left:187px;top:104px;width:78px;">
    <h3>Electrical Inspections</h3>
    <p>PWB can make assessments of your electrical system and equipment and make any safety recommendations needed.</p>
  </div>
  <div class="photo-diamond photo-diamond--inspect" role="img" aria-label="Electrician inspecting wiring" style="left:278px;top:100px;width:36px;height:36px;"></div>
  <div class="photo-diamond photo-diamond--testing" role="img" aria-label="Power quality testing meter" style="left:200px;top:172px;width:36px;height:36px;"></div>
  <div class="copy copy--right" style="left:252px;top:168px;width:84px;">
    <h3>Power Quality Testing</h3>
    <p>PWB has the equipment to run complete power quality testing on your electrical power supply, voice, and data equipment.</p>
  </div>
  <div class="copy" style="left:187px;top:240px;width:78px;">
    <h3>Commercial Services</h3>
    <p>PWB is a full service electrical contractor and provides bucket truck services for exterior building and parking lot lighting. PWB also performs commercial maintenance agreements and emergency services.</p>
  </div>
  <div class="photo-diamond photo-diamond--commercial" role="img" aria-label="Commercial electrical substation" style="left:278px;top:236px;width:36px;height:36px;"></div>

  <div class="copy" style="left:372px;top:26px;width:78px;">
    <h3>Residential Services</h3>
    <p>PWB is a full service electrical contractor providing all forms of electrical services for the residential customer including trouble shooting electrical problems and shorts.</p>
  </div>
  <div class="photo-diamond photo-diamond--residential" role="img" aria-label="Electrician working on a residential panel" style="left:458px;top:28px;width:40px;height:40px;"></div>
  <h2 class="banner banner--right" style="left:405px;top:127px;width:170px;">Specific details</h2>
  <div class="copy copy--justify" style="left:372px;top:152px;width:195px;">
    <p>PWB performs safety inspections, electrical inspections, and code violation inspections also can provide complete home wiring for new construction, remodels and additions or call us if you only need one additional circuit, outlet, switch, ceiling fan, or receptacle installed. No project is too large or small.</p>
    <p>PWB provides electrical service upgrades, complete panel surge protection, lighting additions and energy efficiency recommendations.</p>
  </div>
  <h2 class="banner" style="left:358px;top:272px;width:128px;">Information +</h2>
  <div class="copy" style="left:372px;top:297px;width:195px;">
    <p>Want to know more about what PWB got for you go online and check out our website.</p>
  </div>
  <p class="site-url" style="left:390px;top:318px;">http://www.pwbvoltworks.example/</p>
</section>

</body>
</html>
```